beauty salon

providing waxing services from a home base this must include which I will provide a price list and an address

Industry/Entity Type

Beauty Salon

Font styles to use
Script

Colors

Designer to choose colors to be used in the design.

```html
<!DOCTYPE html>
<html lang="en">
<head>
<meta charset="utf-8">
<title>Tessa's Garden Salon – Beauty Therapist Price List</title>
<link rel="stylesheet" href="https://fonts.googleapis.com/css2?family=Josefin+Sans:wght@300;400;600&family=Arimo:wght@400;700&display=swap">
<style>
  :root {
    --sky-light: #d6eef9;
    --sky-mid: #aedcf1;
    --sky-deep: #86c7e6;
    --plum: #93398f;
    --plum-band: #8a3a8c;
    --ink: #0c1626;
    --navy: #16263f;
    --teal: #1f5f6a;
    --white: #ffffff;
    --skin-light: #f1cdb4;
    --skin-deep: #c98f6e;
  }
  * { margin: 0; padding: 0; box-sizing: border-box; }
  html, body { width: 1200px; height: 850px; overflow: hidden; }
  body { background: var(--sky-light); }

  .flyer {
    position: relative;
    width: 1200px;
    height: 850px;
    overflow: hidden;
    background:
      linear-gradient(135deg, rgba(255,255,255,0.35) 0%, rgba(255,255,255,0) 40%),
      linear-gradient(160deg, var(--sky-light) 0%, var(--sky-mid) 55%, var(--sky-deep) 100%);
    font-family: 'Arimo', Arial, sans-serif;
    color: var(--ink);
  }

  .model-photo {
    position: absolute;
    left: 0; top: 0;
    width: 440px; height: 770px;
    background:
      radial-gradient(ellipse 55% 45% at 50% 55%, var(--skin-light) 0%, rgba(241,205,180,0.6) 60%, rgba(241,205,180,0) 100%),
      linear-gradient(180deg, rgba(201,143,110,0.25), rgba(174,220,241,0));
  }

  .headline {
    position: absolute;
    left: 362px; top: 40px;
    width: 800px;
    font-family: 'Josefin Sans', sans-serif;
    font-weight: 300;
    font-size: 70px;
    letter-spacing: 5px;
    color: var(--white);
    text-align: center;
    white-space: nowrap;
  }
  .subline {
    position: absolute;
    left: 364px; top: 108px;
    width: 795px;
    font-family: 'Josefin Sans', sans-serif;
    font-weight: 400;
    font-size: 22px;
    letter-spacing: 0.5px;
    color: var(--white);
    text-align: center;
    white-space: nowrap;
  }

  .section-title {
    position: absolute;
    left: 440px;
    font-family: 'Josefin Sans', sans-serif;
    font-weight: 400;
    font-size: 36px;
    letter-spacing: 2px;
    color: var(--plum);
    white-space: nowrap;
  }
  .section-title.ladies { top: 176px; }
  .section-title.eyes { top: 466px; }
  .section-title.mens { top: 550px; }

  .price-list {
    position: absolute;
    list-style: none;
    font-weight: 700;
    font-size: 20px;
    letter-spacing: -0.3px;
    color: var(--ink);
  }
  .price-list li {
    position: relative;
    height: 29.8px;
    line-height: 29.8px;
    white-space: nowrap;
  }
  .price-list .price { position: absolute; top: 0; }

  .ladies-a { left: 442px; top: 218px; }
  .ladies-a .price { left: 140px; }
  .ladies-b { left: 687px; top: 218px; }
  .ladies-b .price { left: 171px; }

  .eyes-a { left: 442px; top: 500px; }
  .eyes-a .price { left: 134px; }
  .eyes-b { left: 687px; top: 500px; }
  .eyes-b .price { left: 171px; }

  .mens-a { left: 442px; top: 584px; }
  .mens-a .price { left: 188px; }
  .mens-b { left: 690px; top: 584px; }
  .mens-b .price { left: 165px; }

  .offer-badge {
    position: absolute;
    left: 934px; top: 199px;
    width: 186px; height: 186px;
    border-radius: 50%;
    background: var(--plum);
    color: var(--white);
    text-align: center;
    font-weight: 700;
  }
  .offer-badge .amount {
    display: block;
    margin-top: 28px;
    font-size: 74px;
    line-height: 70px;
    letter-spacing: -2px;
  }
  .offer-badge .terms {
    display: block;
    font-size: 19px;
    line-height: 21px;
  }

  .opening-hours {
    position: absolute;
    left: 920px; top: 430px;
    width: 242px;
    text-align: center;
    font-weight: 700;
    font-size: 20px;
    line-height: 29.6px;
    color: var(--plum);
  }
  .opening-hours .label { color: var(--navy); }

  .salon-mark {
    position: absolute;
    left: 836px; top: 660px;
    width: 360px;
    text-align: center;
  }
  .salon-mark .dot {
    display: block;
    width: 54px; height: 54px;
    margin: 0 auto 10px;
    border-radius: 50%;
    background: var(--teal);
    opacity: 0.75;
  }
  .salon-mark .name {
    font-family: 'Josefin Sans', sans-serif;
    font-weight: 400;
    font-size: 29px;
    color: var(--navy);
    white-space: nowrap;
  }

  .contact-band {
    position: absolute;
    left: 0; top: 770px;
    width: 1200px; height: 80px;
    background: var(--plum-band);
    color: var(--white);
  }
  .contact-band .mobile {
    position: absolute;
    left: 42px; top: 21px;
    font-weight: 700;
    font-size: 34px;
    letter-spacing: -0.3px;
  }
  .contact-band .address {
    position: absolute;
    left: 644px; top: 25px;
    font-family: 'Josefin Sans', sans-serif;
    font-weight: 400;
    font-size: 29px;
    letter-spacing: 1.5px;
    white-space: nowrap;
  }
</style>
</head>
<body>
<main class="flyer">
  <div class="model-photo" role="img" aria-label="Photograph of a smiling woman in a cream bikini, arms raised, against a light blue background"></div>

  <h1 class="headline">BEAUTY THERAPIST</h1>
  <p class="subline">TESSA DIPLOMA OF BEAUTY THERAPY AT MARLOW INSTITUTE</p>

  <h2 class="section-title ladies">LADY'S WAXING</h2>
  <ul class="price-list ladies-a">
    <li>Eyebrow<span class="price">$8</span></li>
    <li>Upper lip<span class="price">$8</span></li>
    <li>Chin<span class="price">$8</span></li>
    <li>Face wax<span class="price">$25</span></li>
    <li>Bikini line<span class="price">$15</span></li>
    <li>G string<span class="price">$20</span></li>
    <li>½ Brazilian<span class="price">$30</span></li>
  </ul>
  <ul class="price-list ladies-b">
    <li>Full Brazilian<span class="price">$40</span></li>
    <li>Half arm<span class="price">$20</span></li>
    <li>Upper half arm<span class="price">$20</span></li>
    <li>Full arm<span class="price">$25</span></li>
    <li>Half leg<span class="price">$15</span></li>
    <li>Upper leg<span class="price">$20</span></li>
    <li>¾ Leg<span class="price">$25</span></li>
    <li>Full leg<span class="price">$35</span></li>
  </ul>

  <h2 class="section-title eyes">EYE ENHANCEMENT</h2>
  <ul class="price-list eyes-a">
    <li>Eyebrow Tint<span class="price">$12</span></li>
  </ul>
  <ul class="price-list eyes-b">
    <li>Eyelash Tint<span class="price">$15</span></li>
  </ul>

  <h2 class="section-title mens">MEN'S WAXING</h2>
  <ul class="price-list mens-a">
    <li>Eyebrow<span class="price">$10</span></li>
    <li>Half arm<span class="price">$20</span></li>
    <li>Upper half arm<span class="price">$25</span></li>
    <li>Full arm<span class="price">$30</span></li>
    <li>Half leg<span class="price">$25</span></li>
  </ul>
  <ul class="price-list mens-b">
    <li>Full leg<span class="price">$45</span></li>
    <li>Chest wax<span class="price">$40</span></li>
    <li>Back wax<span class="price">$35</span></li>
  </ul>

  <div class="offer-badge">
    <span class="amount">10%</span>
    <span class="terms">Discount on<br>first treatment.</span>
  </div>

  <div class="opening-hours">
    <div class="label">NOW OPEN:</div>
    <div>Wednesday</div>
    <div>10am - 4pm</div>
    <div>Fridays</div>
    <div>10am - 7pm</div>
    <div>Saturday 10am - 4pm</div>
  </div>

  <div class="salon-mark">
    <span class="dot"></span>
    <span class="name">Tessa's Garden Salon</span>
  </div>

  <footer class="contact-band">
    <span class="mobile">Mobile: 0400 555 018</span>
    <span class="address">12 FINCH LANE - HARBOUR VALE</span>
  </footer>
</main>
</body>
</html>
```